Business Card

I need a business card for a nutrition/fitness consultant. We are a personalized and online service that caters to developing individual plans based on persons needs. I will send you information to need on card as well as logo. Last business card was grey background and writing was black and red. I think a pic on the backside (maybe a photo that is on the app) would be good?

HelloMarlo (Ill send you logo)
Marlo Venti, Registered Nurse and Certified Sports Nutrionist (R.N., C.S.N.)
Personalized Nutrition and Fitness Architecture

1-800-555-0147 office
(305) 555-0182 cell
website www.hellomarlo-demo.com
marlo@hellomarlo-demo.com

Two locations so maybe two cards
2180 Willowbend Lane, inside Sunpeak Glow Studio
Coral Gables, Fl 33199

and
7300 W Orchard Parkway
Boca Raton, Florida 33498

Requirements
Must have
• I guess the logo we provide so it is consistent with the new website etc

```html
<!DOCTYPE html>
<html lang="en">
<head>
<meta charset="utf-8">
<title>HelloMarlo Business Card</title>
<link rel="stylesheet" href="https://fonts.googleapis.com/css2?family=Open+Sans:wght@400;600;700&display=swap">
<style>
  :root {
    --red: #e51b33;
    --red-light: #f0475a;
    --black: #121212;
    --charcoal: #2a2a2a;
    --white: #ffffff;
    --page: #ececec;
    --photo-light: #f2f2f2;
    --photo-mid: #a9a9a9;
  }
  * { margin: 0; padding: 0; box-sizing: border-box; }
  html, body { width: 1200px; height: 1024px; overflow: hidden; }
  body {
    background: var(--page);
    font-family: "Open Sans", sans-serif;
    position: relative;
  }
  .card {
    position: absolute;
    top: 152px;
    width: 420px;
    height: 720px;
    overflow: hidden;
    box-shadow: 0 10px 30px rgba(0,0,0,0.25);
  }
  .card--front { left: 150px; }
  .card--back { left: 630px; }
  .card__art { position: absolute; inset: 0; display: block; }

  .identity {
    position: absolute;
    top: 62px;
    right: 34px;
    text-align: right;
  }
  .identity__name {
    font-weight: 700;
    font-size: 30px;
    color: var(--black);
    line-height: 1.1;
    margin-bottom: 6px;
  }
  .identity__title {
    color: var(--white);
    font-size: 20px;
    line-height: 1.28;
  }

  .contact {
    position: absolute;
    top: 372px;
    right: 34px;
    text-align: right;
    color: var(--white);
    font-size: 19px;
    line-height: 1.3;
  }
  .contact__label { color: var(--red); font-weight: 700; }
  .contact__web { font-weight: 700; font-size: 22px; margin-bottom: 18px; }
  .contact__web span { color: var(--red); }
  .contact__address { margin-bottom: 4px; }

  .brand {
    position: absolute;
    top: 420px;
    right: 36px;
    display: flex;
    align-items: center;
    gap: 10px;
  }
  .brand__dot {
    width: 22px; height: 22px; border-radius: 50%;
    background: var(--red);
  }
  .brand__name {
    font-weight: 700;
    font-size: 40px;
    color: var(--charcoal);
  }
</style>
</head>
<body>

<section class="card card--front">
  <svg class="card__art" viewBox="0 0 420 720" aria-hidden="true">
    <defs>
      <linearGradient id="gloss" x1="0" y1="0" x2="1" y2="1">
        <stop offset="0" stop-color="#3a3a3a"/>
        <stop offset="0.5" stop-color="#111"/>
        <stop offset="1" stop-color="#000"/>
      </linearGradient>
    </defs>
    <rect width="420" height="720" fill="var(--red)"/>
    <path d="M0 0 H420 V38 Q190 20 0 118 Z" fill="var(--black)"/>
    <circle cx="262" cy="650" r="335" fill="url(#gloss)"/>
    <path d="M0 690 Q210 700 420 660 V720 H0 Z" fill="var(--black)"/>
  </svg>

  <header class="identity">
    <h1 class="identity__name">Marlo Venti</h1>
    <p class="identity__title">Registered Nurse &amp; Certified<br>Sports Nutrionist (R.N., C.S.N.)<br>Personalized Nutrition &amp;<br>Fitness Architecture</p>
  </header>

  <address class="contact" style="font-style:normal">
    <p><span class="contact__label">office</span> 1-800-555-0147</p>
    <p><span class="contact__label">cell</span> (305) 555-0182</p>
    <p><span class="contact__label">email</span> marlo@hellomarlo-demo.com</p>
    <p class="contact__web">www.<span>hellomarlo-demo</span>.com</p>
    <p class="contact__address">2180 Willowbend Lane,<br>inside Sunpeak Glow Studio<br>Coral Gables, Fl 33199</p>
    <p class="contact__address">7300 W Orchard Parkway<br>Boca Raton, Florida 33498</p>
  </address>
</section>

<section class="card card--back">
  <svg class="card__art" viewBox="0 0 420 720" aria-hidden="false">
    <defs>
      <linearGradient id="photoTone" x1="0" y1="0" x2="1" y2="1">
        <stop offset="0" stop-color="var(--photo-mid)"/>
        <stop offset="0.55" stop-color="var(--photo-light)"/>
        <stop offset="1" stop-color="#d8d8d8"/>
      </linearGradient>
    </defs>
    <rect width="420" height="720" fill="var(--red)"/>
    <g role="img" aria-label="Black and white portrait photo of the consultant holding a red apple, with a bowl of red apples">
      <path d="M70 110 H420 V560 H70 Q20 560 20 335 Q20 110 70 110 Z" fill="url(#photoTone)"/>
    </g>
    <path d="M0 0 H420 V70 Q200 40 0 170 Z" fill="var(--red)"/>
    <path d="M0 470 Q200 520 420 600 V720 H0 Z" fill="var(--red)"/>
    <path d="M0 610 Q220 620 420 690 V720 H0 Z" fill="var(--black)"/>
  </svg>

  <div class="brand">
    <span class="brand__dot"></span>
    <span class="brand__name">HelloMarlo</span>
  </div>
</section>

</body>
</html>
```